Vel Techniqos Logo Design

We need a business card design for Las Vegas based company called "Vel Techniqs" (http://www.veltechniqs-example.com). Vel Techniqs prides itself in providing in-depth knowledge that is based on real-world experience in the field of wireless telecommunications. Our practice covers strategy, marketing, and business development across the entire telecom value chain – from consumer to enterprise, content to applications, and mobile devices to wireless infrastructure. Our expertise is in the fields of wireless telecommunications, network optimization, specializing in CDMA, UMTS, WiMAX and LTE solutions.
The logo attached could be reused for the business card, but would prefer a new innovative logo as well. The final design should project cutting edge wireless technologies. The design should also communicate a modern business that has expertise and is focused on R&D.
Updates

Team,

  Forgot to mention this.  While Vel Techniqs is focused in wireless technologies, the word 'Vel' comes from Hindi language and means harmonious music

Project Deadline Extended
Reason: Extending deadline to allow for the designer to complete final changes. Thank you all for submitting the designs so far. Thanks, Rohan.

Industry/Entity Type

Business

Logo Text

Vel Techniqs

```html
<!DOCTYPE html>
<html lang="en">
<head>
<meta charset="utf-8">
<title>Vel Techniqs Business Card</title>
<link href="https://fonts.googleapis.com/css2?family=Lato:wght@400;700&family=Roboto+Condensed:wght@400&display=swap" rel="stylesheet">
<style>
  :root {
    --page-bg: #d9d9d9;
    --card-bg: #333333;
    --card-edge: #2a2a2a;
    --accent-blue: #3a7fc4;
    --mark-grey: #6f6f6f;
    --text-white: #ffffff;
    --badge-tone: #4f8fc9;
  }
  * { box-sizing: border-box; margin: 0; padding: 0; }
  html, body {
    width: 1200px;
    height: 1000px;
    overflow: hidden;
    background: var(--page-bg);
  }
  .canvas {
    position: relative;
    width: 1200px;
    height: 1000px;
  }
  .card {
    position: absolute;
    left: 220px;
    width: 760px;
    height: 434px;
    background: var(--card-bg);
    border: 1px solid var(--card-edge);
    box-shadow: 0 6px 18px rgba(0,0,0,0.25);
    display: flex;
    flex-direction: column;
    align-items: center;
  }
  .card--front { top: 46px; padding-top: 70px; }
  .card--back { top: 520px; padding-top: 34px; }

  .brand-dot {
    border-radius: 50%;
    background: var(--badge-tone);
    flex: none;
  }
  .card--front .brand-dot { width: 170px; height: 170px; }
  .card--back .brand-dot { width: 104px; height: 104px; }

  .wordmark {
    font-family: "Lato", sans-serif;
    font-weight: 400;
    color: var(--mark-grey);
    letter-spacing: 0.08em;
    text-transform: uppercase;
    line-height: 1;
    white-space: nowrap;
  }
  .card--front .wordmark { font-size: 54px; margin-top: 26px; }
  .card--back .wordmark { font-size: 36px; margin-top: 16px; }

  .tagline {
    font-family: "Roboto Condensed", sans-serif;
    font-size: 24px;
    color: var(--text-white);
    margin-top: 16px;
    letter-spacing: 0.02em;
    white-space: nowrap;
  }

  .person-name {
    font-family: "Lato", sans-serif;
    font-weight: 700;
    font-size: 27px;
    color: var(--text-white);
    margin-top: 26px;
    line-height: 1;
  }
  .person-title {
    font-family: "Lato", sans-serif;
    font-size: 19px;
    color: var(--accent-blue);
    margin-top: 4px;
  }
  .contact-list {
    list-style: none;
    margin-top: 14px;
    text-align: center;
    font-family: "Lato", sans-serif;
    font-size: 21px;
    line-height: 1.3;
    color: var(--text-white);
    white-space: nowrap;
  }
  .contact-label { color: var(--accent-blue); font-style: italic; }
</style>
</head>
<body>
<main class="canvas">
  <section class="card card--front">
    <div class="brand-dot" aria-hidden="true"></div>
    <h1 class="wordmark">Vel Techniqs</h1>
    <p class="tagline">Where Others Offer Services, We Engineer Answers!</p>
  </section>

  <section class="card card--back">
    <div class="brand-dot" aria-hidden="true"></div>
    <h2 class="wordmark">Vel Techniqs</h2>
    <p class="person-name">YOUR NAME</p>
    <p class="person-title">Title</p>
    <ul class="contact-list">
      <li><span class="contact-label">Phone:</span> 123 456 7890</li>
      <li><span class="contact-label">Email:</span> yourname@veltechniqs-example.com</li>
      <li><span class="contact-label">Website:</span> www.veltechniqsllc-example.com</li>
    </ul>
  </section>
</main>
</body>
</html>
```